Short term vacation rental

I need a simple site the we can rent a duplex that is on the sand in Indian rocks beach Fl needs to be able to sync with multiple calendars like tarnivo.com qelm zunt using Wordpress

```html
<!DOCTYPE html>
<html lang="en">
<head>
<meta charset="utf-8">
<title>Sandpiper Shores – Beachfront Duplex</title>
<link href="https://fonts.googleapis.com/css2?family=Roboto:wght@300;400;500;700&display=swap" rel="stylesheet">
<style>
:root{
  --teal:#55a6ab;
  --teal-dark:#3f8f95;
  --navy:#1f3762;
  --navy-bar:#1c4a8a;
  --ink:#233352;
  --text:#8a8f98;
  --line:#e5e7ea;
  --gold:#d6b24a;
  --footer:#1c1c1e;
  --white:#fff;
}
*{box-sizing:border-box;margin:0;padding:0}
html,body{width:1200px;height:4446px;overflow:hidden}
body{position:relative;font-family:"Roboto",sans-serif;color:var(--text);background:var(--white)}
.abs{position:absolute}
.photo{position:absolute}
h2.section-title{position:absolute;left:0;width:1200px;text-align:center;font-weight:400;font-size:34px;color:var(--ink)}
h2 .accent,h3 .accent{color:var(--teal)}
.lead{position:absolute;left:0;width:1200px;text-align:center;font-size:13px;font-weight:300;color:var(--text)}
.btn{position:absolute;display:flex;align-items:center;justify-content:center;font-size:13px;font-weight:500;color:var(--white);letter-spacing:.3px;text-transform:uppercase}
.btn.teal{background:var(--teal)}
.btn.navy{background:var(--navy)}

/* header */
.site-header{position:absolute;left:0;top:0;width:1200px;height:90px;background:var(--white)}
.brand{position:absolute;left:70px;top:32px;display:flex;align-items:center;gap:8px;font-size:19px;font-weight:500;color:var(--navy);letter-spacing:.5px}
.brand .dot{width:10px;height:10px;border-radius:50%;background:var(--teal)}
.main-nav a{position:absolute;top:36px;font-size:13px;color:#333;text-decoration:none;text-transform:uppercase}
.main-nav a.active{color:var(--teal)}
.main-nav .underline{position:absolute;left:390px;top:87px;width:56px;height:3px;background:var(--teal)}

/* hero */
.hero{position:absolute;left:0;top:90px;width:1200px;height:526px;background:linear-gradient(180deg,#8dbbe0 0%,#cfe3f0 40%,#d9d3c4 58%,#2f8fc0 70%,#1f74a6 100%)}
.hero .sub{position:absolute;left:0;top:138px;width:1200px;text-align:center;font-size:33px;font-weight:300;color:var(--white);letter-spacing:1px}
.hero .title{position:absolute;left:0;top:193px;width:1200px;text-align:center;font-size:56px;font-weight:700;color:var(--white);letter-spacing:6px}
.hero-dots{position:absolute;left:530px;top:472px;display:flex;gap:9px;align-items:center}
.hero-dots span{width:10px;height:10px;background:rgba(255,255,255,.6)}
.hero-dots span.on{background:var(--white)}

/* availability */
.availability{position:absolute;left:0;top:616px;width:1200px;height:111px;background:var(--navy)}
.availability .label{position:absolute;left:0;top:0;width:276px;height:111px;background:var(--teal);padding:26px 0 0 69px;font-size:24px;font-weight:500;color:var(--white);line-height:30px}
.availability .go{position:absolute;left:262px;top:40px;width:30px;height:30px;border-radius:50%;background:var(--white)}
.field{position:absolute;top:38px;height:35px;border:1px solid #6f87ad;display:flex;align-items:center;padding-left:17px;font-size:12px;font-weight:700;color:var(--white)}
.field .cal{position:absolute;right:0;top:0;width:35px;height:33px;background:var(--teal)}
.field svg.chev{position:absolute;right:14px;top:12px}
.availability .btn{top:38px;height:35px;font-size:12px;font-weight:700}

/* about */
.about-copy p{font-size:13px;line-height:23px;font-weight:300;color:var(--text)}
h3.block-title{position:absolute;font-weight:400;font-size:28px;color:var(--ink)}
h3.block-title.bold{font-weight:500;font-size:35px}

/* services */
.service{position:absolute;display:flex;align-items:center;font-size:13px;font-weight:300}
.service .ico{width:44px;height:44px;border:1px solid var(--navy);display:flex;align-items:center;justify-content:center;margin-right:17px}

/* testimonial */
.testimonial{position:absolute;left:0;top:2372px;width:1200px;height:292px;background:linear-gradient(180deg,#1f2a33,#2e3a3e 60%,#3b3a2f)}
.testimonial .name{position:absolute;left:426px;top:41px;font-size:20px;font-weight:500;color:var(--white);letter-spacing:.5px}
.testimonial .quote{position:absolute;left:426px;top:96px;width:720px;font-size:14px;line-height:18px;font-weight:300;color:#e8e8e8}
.t-dots span{position:absolute;left:377px;border-radius:50%;background:var(--white)}
.social-round{position:absolute;width:50px;height:50px;border-radius:50%}

/* events */
.countdown{position:absolute;left:69px;top:2885px;width:66px;height:307px;border:2px solid var(--teal);border-right:none}
.countdown .unit{position:absolute;left:0;width:64px;text-align:center}
.countdown .num{font-size:24px;color:#333;font-weight:400}
.countdown .lbl{font-size:11px;color:#555}
.countdown .sep{position:absolute;left:16px;width:36px;height:1px;background:var(--line)}
.card{position:absolute;top:2868px;width:252px}
.card .pic{position:relative;width:252px;height:223px}
.card .date{position:absolute;left:11px;top:174px;width:44px;height:48px;background:var(--navy);color:var(--white);text-align:center;font-size:18px;font-weight:700;line-height:20px;padding-top:5px}
.card .date small{display:block;font-size:11px;font-weight:500}
.card .meta{margin-top:22px;font-size:11px;color:#333;display:flex;justify-content:space-between}
.card .meta em{font-style:normal;color:var(--text)}
.card h4{margin-top:28px;font-size:16px;font-weight:400;color:#222;line-height:19px}
.card p{margin-top:14px;font-size:11px;line-height:15px;font-weight:300;color:var(--text)}
.card .more{margin-top:18px;font-size:11px;font-weight:700;color:var(--teal)}

/* gallery */
.gallery{position:absolute;left:0;top:3514px;width:1200px;height:414px;display:grid;grid-template-columns:repeat(6,200px);grid-template-rows:207px 207px}

/* newsletter */
.newsletter{position:absolute;left:0;top:4042px;width:1200px;height:76px;background:var(--navy-bar)}
.newsletter .title{position:absolute;left:133px;top:24px;font-size:22px;font-weight:500;color:var(--white);letter-spacing:.5px}
.newsletter .ring{position:absolute;left:73px;top:18px;width:40px;height:40px;border:2px solid var(--gold);border-radius:50%}
.newsletter .input{position:absolute;left:382px;top:19px;width:266px;height:35px;border:2px solid var(--white);padding:9px 10px;font-size:11px;color:var(--white)}
.newsletter .btn{left:661px;top:19px;width:183px;height:35px;background:var(--gold);font-size:12px}
.newsletter .soc{position:absolute;top:24px;width:29px;height:29px;border:2px solid var(--white);border-radius:50%}

/* footer */
.site-footer{position:absolute;left:0;top:4118px;width:1200px;height:328px;background:var(--footer);color:#bbb}
.site-footer h5{position:absolute;top:24px;font-size:18px;font-weight:500;color:var(--white)}
.site-footer ul{position:absolute;top:82px;list-style:none;font-size:14px;line-height:34px;font-weight:300;color:#ccc}
.site-footer .about-txt{position:absolute;left:69px;top:80px;width:260px;font-size:12px;line-height:15px;color:#bbb}
.site-footer .contact{position:absolute;left:69px;display:flex;gap:16px;font-size:12px;line-height:14px;color:#ddd}
.blog{position:absolute;left:837px;width:293px}
.blog strong{display:block;font-size:13px;font-weight:700;color:var(--white)}
.blog p{width:170px;margin-top:8px;font-size:10px;line-height:12px;color:#bbb}
.blog .thumb{position:absolute;left:197px;top:0;width:96px;height:96px}
</style>
</head>
<body>

<header class="site-header">
  <div class="brand"><span class="dot"></span>Sandpiper Shores</div>
  <nav class="main-nav">
    <a class="active" style="left:390px">Home</a>
    <a style="left:474px">About Us</a>
    <a style="left:586px">The Duplex</a>
    <a style="left:716px">Rooms</a>
    <a style="left:808px">Review</a>
    <a style="left:903px">Gallery</a>
    <a style="left:1008px">Contact Us</a>
    <span class="underline"></span>
  </nav>
</header>

<section class="hero" role="img" aria-label="Beachfront resort pool with thatched umbrellas and white villa balconies under a blue sky">
  <div class="sub">YOUR BEACHFRONT</div>
  <div class="title">ESCAPE AWAITS</div>
  <div class="btn navy" style="left:506px;top:285px;width:186px;height:45px;font-size:15px">Book Your Stay</div>
  <div class="hero-dots">
    <svg width="12" height="18" viewBox="0 0 12 18"><path d="M9 2 2 9l7 7" fill="none" stroke="#fff" stroke-width="2"/></svg>
    <span></span><span></span><span class="on"></span><span></span><span></span>
    <svg width="12" height="18" viewBox="0 0 12 18"><path d="m3 2 7 7-7 7" fill="none" stroke="#fff" stroke-width="2"/></svg>
  </div>
</section>

<section class="availability">
  <div class="label">CHECK<br>AVAILABILITY</div>
  <div class="go"><svg width="30" height="30" viewBox="0 0 30 30"><path d="m13 9 6 6-6 6" fill="none" stroke="#999" stroke-width="2"/></svg></div>
  <div class="field" style="left:311px;width:181px">Arrival Date<span class="cal"></span></div>
  <div class="field" style="left:501px;width:181px">Departure Date<span class="cal"></span></div>
  <div class="field" style="left:696px;width:121px">Adult<svg class="chev" width="12" height="8" viewBox="0 0 12 8"><path d="m1 1 5 5 5-5" fill="none" stroke="#fff" stroke-width="1.5"/></svg></div>
  <div class="field" style="left:829px;width:124px">Children<svg class="chev" width="12" height="8" viewBox="0 0 12 8"><path d="m1 1 5 5 5-5" fill="none" stroke="#fff" stroke-width="1.5"/></svg></div>
  <div class="btn teal" style="left:963px;width:166px">Check Availability</div>
</section>

<h2 class="section-title" style="top:776px">Welcome to <span class="accent" style="font-weight:500">Sandpiper Shores</span></h2>
<svg class="abs" style="left:426px;top:838px" width="348" height="12" viewBox="0 0 348 12"><line x1="0" y1="6" x2="148" y2="6" stroke="#1f3762"/><line x1="200" y1="6" x2="348" y2="6" stroke="#1f3762"/><circle cx="160" cy="6" r="2.5" fill="#55a6ab"/><circle cx="174" cy="6" r="4" fill="#55a6ab"/><circle cx="188" cy="6" r="2.5" fill="#55a6ab"/></svg>
<p class="lead" style="top:871px">Lorem Ipsum is simply dummy text of the printing and typesetting industry.</p>

<div class="photo" style="left:69px;top:958px;width:230px;height:392px;background:linear-gradient(180deg,#7fb0da,#e9e6df 45%,#3f9fcf 80%,#2a82b8)" role="img" aria-label="Guest standing by the pool in front of a white villa"></div>
<div class="photo" style="left:319px;top:958px;width:230px;height:392px;background:linear-gradient(180deg,#3f7fc9,#e8e8e4 50%,#6a8a5a 80%,#b9b2a2)" role="img" aria-label="White villa facade with palm trees"></div>
<h3 class="block-title" style="left:596px;top:987px">About <span class="accent">US</span></h3>
<div class="abs about-copy" style="left:596px;top:1040px;width:520px">
  <p>Coral Haven Group was established to cater to the growing demand for high-quality accommodation from both Gulf Coast travellers and foreign tourists. Coral Haven Group was established since 2002 as a subsidiary of Coral Haven Holding Co.,Ltd. The group has Coral Haven Inn (Tidewater).</p>
  <p style="margin-top:12px">Coral Haven Group was established to cater to the growing demand for high-quality accommodation from both Gulf Coast travellers and foreign tourists. Coral Haven Group was established since 2002 as a subsidiary of Coral Haven Holding Co.,Ltd. The group has Coral Haven Inn (Tidewater).</p>
</div>
<div class="btn teal" style="left:596px;top:1272px;width:145px;height:37px">Read More</div>

<h3 class="block-title bold" style="left:69px;top:1452px">Take A <span class="accent">Look Inside</span></h3>
<div class="abs" style="left:69px;top:1522px;width:500px;font-size:13.5px;line-height:17.5px;font-weight:300;color:var(--text)">
  <p>After a long drive or flight, you want to arrive at a place that feels like home. In Tidewater, that place is Coral Haven Inn (Tidewater). Our 90 spacious rooms are set on acres of well-tended gardens that are fresh and green all year round. Conveniently located, with stylishly appointed rooms and all the facilities a business traveler expects, Coral Haven Inn (Tidewater) is the smart choice for visitors to the capital city.</p>
  <p style="margin-top:21px">The hotel features 90 rooms, including 48 Superior Rooms, 4 Junior Suites, a Suite Room, 30 Superior Villas, 4 Suite Villas, 2 Executive Villas and a Presidential Villa. From a majestic four bedroom presidential suite, to the modern and cosy superior rooms, Coral Haven's famed teak has been employed liberally to give the rooms a distinctive local flavor and classic look.</p>
</div>
<div class="btn teal" style="left:69px;top:1806px;width:145px;height:36px">Book Now</div>
<div class="photo" style="left:596px;top:1462px;width:259px;height:197px;background:linear-gradient(135deg,#8a7f6c,#c9c1ad 50%,#6d6558)" role="img" aria-label="Interior dining area with wooden chairs"></div>
<div class="photo" style="left:865px;top:1462px;width:266px;height:197px;background:linear-gradient(180deg,#8fb7dc,#3f7fa6 45%,#4fb6d6 75%,#c8c2b0)" role="img" aria-label="Pool overlooking the sea and lighthouse"></div>
<div class="photo" style="left:596px;top:1678px;width:259px;height:197px;background:linear-gradient(180deg,#3b3a36,#6f8a4a 40%,#e4e1da 60%,#d6d2ca)" role="img" aria-label="Potted plant on a white cabinet"></div>
<div class="photo" style="left:865px;top:1678px;width:266px;height:197px;background:linear-gradient(180deg,#7fb1df,#e8e8e4 55%,#3d9ccc 85%)" role="img" aria-label="White villa arches beside the pool"></div>

<div class="photo" style="left:69px;top:1949px;width:489px;height:349px;background:radial-gradient(ellipse at 50% 55%,#7a5a3a 0%,#3a2a1e 40%,#0e0c0b 75%)" role="img" aria-label="Grilled seafood and vegetables on a tabletop barbecue"></div>
<h3 class="block-title bold" style="left:596px;top:1940px">Our <span class="accent">Best Services</span></h3>
<p class="abs" style="left:596px;top:2008px;width:520px;font-size:13.5px;line-height:17.5px;font-weight:300">Lorem Ipsum is simply dummy text of the printing and typesetting industry. Lorem Ipsum has been the industry's standard dummy text ever since the 1500s,</p>

<div class="service" style="left:597px;top:2100px"><span class="ico"><svg width="20" height="20" viewBox="0 0 20 20"><path d="M5 8h10v6a4 4 0 0 1-4 4H9a4 4 0 0 1-4-4zM7 4v2M10 3v3M13 4v2" fill="none" stroke="#55a6ab" stroke-width="1.5"/></svg></span>Coffee maker</div>
<div class="service" style="left:872px;top:2100px"><span class="ico"><svg width="20" height="20" viewBox="0 0 20 20"><circle cx="10" cy="10" r="8" fill="none" stroke="#55a6ab" stroke-width="1.5"/><path d="M8 6v8l6-4z" fill="#55a6ab"/></svg></span>25 inch larger TV</div>
<div class="service" style="left:597px;top:2166px"><span class="ico"><svg width="20" height="20" viewBox="0 0 20 20"><rect x="7" y="2" width="6" height="10" rx="3" fill="none" stroke="#55a6ab" stroke-width="1.5"/><path d="M4 10a6 6 0 0 0 12 0M10 16v3" fill="none" stroke="#55a6ab" stroke-width="1.5"/></svg></span>Cable/Satellite TV channels</div>
<div class="service" style="left:872px;top:2166px"><span class="ico"><svg width="20" height="20" viewBox="0 0 20 20"><rect x="6" y="2" width="8" height="16" rx="1" fill="none" stroke="#55a6ab" stroke-width="1.5"/><path d="M8 8h4M8 11h4" stroke="#55a6ab" stroke-width="1.5"/></svg></span>AM/FM clock radio</div>
<div class="service" style="left:597px;top:2232px"><span class="ico"><svg width="20" height="20" viewBox="0 0 20 20"><path d="M4 3l3 0 2 4-2 2a10 10 0 0 0 4 4l2-2 4 2v3a2 2 0 0 1-2 2A14 14 0 0 1 2 5a2 2 0 0 1 2-2z" fill="none" stroke="#55a6ab" stroke-width="1.5"/></svg></span>Oversized work desk</div>
<div class="service" style="left:872px;top:2232px"><span class="ico"><svg width="20" height="20" viewBox="0 0 20 20"><circle cx="10" cy="10" r="8" fill="none" stroke="#55a6ab" stroke-width="1.5"/><path d="M10 5v5l3 2" fill="none" stroke="#55a6ab" stroke-width="1.5"/></svg></span>24-Hour Concierge service</div>

<section class="testimonial">
  <div class="photo" style="left:0;top:0;width:383px;height:292px;background:linear-gradient(135deg,#e9e6e2,#c7c0b8 60%,#a79d93)" role="img" aria-label="Portrait of a smiling guest"></div>
  <div class="t-dots">
    <span style="top:116px;width:12px;height:12px;left:377px"></span>
    <span style="top:136px;width:18px;height:18px;left:374px;background:var(--teal)"></span>
    <span style="top:162px;width:12px;height:12px;left:377px"></span>
  </div>
  <div class="name">ELIAN MARSH CORBETT</div>
  <p class="quote">Lorem Ipsum is simply dummy text of the printing and typesetting industry. Lorem Ipsum has been the industry's standard dummy text ever since the 1500s, when an unknown printer took a galley of type and scrambled it to make a type specimen book. It has survived not only five centuries, but also the leap into electronic typesetting, remaining essentially unchanged.</p>
  <span class="social-round" style="left:705px;top:207px;background:#3b5a9a"></span>
  <span class="social-round" style="left:766px;top:207px;background:#d9503f"></span>
  <span class="social-round" style="left:826px;top:207px;background:#1da1f2"></span>
</section>

<h2 class="section-title" style="top:2730px;font-weight:500">Latest <span class="accent">Events &amp; News</span></h2>
<p class="lead" style="top:2800px">Lorem Ipsum is simply dummy text of the printing and typesetting industry.</p>

<div class="countdown">
  <div class="unit" style="top:16px"><div class="num">11</div><div class="lbl">Days</div></div>
  <span class="sep" style="top:78px"></span>
  <div class="unit" style="top:92px"><div class="num">06</div><div class="lbl">Hours</div></div>
  <span class="sep" style="top:154px"></span>
  <div class="unit" style="top:168px"><div class="num">56</div><div class="lbl">Mins</div></div>
  <span class="sep" style="top:230px"></span>
  <div class="unit" style="top:244px"><div class="num">31</div><div class="lbl">Sec</div></div>
</div>
<div class="photo" style="left:154px;top:2868px;width:430px;height:489px;background:radial-gradient(ellipse at 45% 25%,#e8b05a,#8a4a22 45%,#3a1d12 80%)" role="img" aria-label="Candlelit restaurant table with wine glasses"></div>

<article class="card" style="left:611px">
  <div class="pic" style="background:linear-gradient(180deg,#7a1414,#3a0a0a 60%,#1a1414)" role="img" aria-label="Red lounge interior with wine shelves"><div class="date">26<small>FEB</small></div></div>
  <div class="meta"><span><em>Posted By:</em> Tessa Vale</span><em>♡14 | ✎08</em></div>
  <h4>The lightning no one you see is the smarter than black</h4>
  <p>They call him Flipper than lightning no one you see is smarter than he black gold all of them had hair of gold like their mother the young one in curls.</p>
  <div class="more">READ MORE ›</div>
</article>
<article class="card" style="left:877px">
  <div class="pic" style="background:linear-gradient(180deg,#5a1a4a,#2a1420 55%,#7a2a1a)" role="img" aria-label="Purple-lit lounge with a wall screen and red seating"><div class="date">26<small>MAR</small></div></div>
  <div class="meta"><span><em>Posted By:</em> Tessa Vale</span><em>♡14 | ✎08</em></div>
  <h4>The lightning no one you see is the smarter than black</h4>
  <p>They call him Flipper than lightning no one you see is smarter than he black gold all of them had hair of gold like their mother the young one in curls.</p>
  <div class="more">READ MORE ›</div>
</article>

<h2 class="section-title" style="top:3424px;font-weight:500">Our <span class="accent">Gallery</span></h2>
<span class="abs" style="left:561px;top:3483px;width:78px;height:2px;background:#e3c3a8"></span>
<section class="gallery">
  <div role="img" aria-label="Sandy beach under a cloudy sky" style="background:linear-gradient(180deg,#c9d3da,#9fb0b8 50%,#c8b79a)"></div>
  <div role="img" aria-label="Guest in sunglasses at the waterfront" style="background:linear-gradient(135deg,#4f8fc9,#c9a98a 55%,#6a5a4a)"></div>
  <div role="img" aria-label="Coastal road along the hills" style="background:linear-gradient(180deg,#5fa0d8,#c8d8e0 45%,#6a7a5a 75%,#3a3a36)"></div>
  <div role="img" aria-label="Bright bedroom with white linens" style="background:linear-gradient(180deg,#eeeae4,#d6cfc4 60%,#a7a19a)"></div>
  <div role="img" aria-label="Turquoise water with a boat" style="background:linear-gradient(180deg,#1fb2c0,#5fd0d2 60%,#2a9ab0)"></div>
  <div role="img" aria-label="Beach with a pier" style="background:linear-gradient(180deg,#bcd8ec,#4fb5c8 55%,#e4dcc8)"></div>
  <div role="img" aria-label="Shoreline and sand" style="background:linear-gradient(180deg,#8fbfe0,#5a9ab0 40%,#d8c49a)"></div>
  <div role="img" aria-label="Bedroom with a carved headboard" style="background:linear-gradient(180deg,#cdbba0,#eae4dc 50%,#b09a80)"></div>
  <div role="img" aria-label="Town on the coast at dusk" style="background:linear-gradient(180deg,#3a8ac9,#9ac0d8 55%,#4a4a42)"></div>
  <div role="img" aria-label="Hotel room with curtains and beds" style="background:linear-gradient(180deg,#c08a5a,#e8e0d4 55%,#8a6a50)"></div>
  <div role="img" aria-label="White villa balconies by the sea" style="background:linear-gradient(180deg,#3f8ad0,#ececea 50%,#2aa0cc)"></div>
  <div role="img" aria-label="Waves on a quiet beach" style="background:linear-gradient(180deg,#d0d6da,#9aa8ac 45%,#d8c8a8)"></div>
</section>
<div class="btn teal" style="left:499px;top:3966px;width:200px;height:36px">Browse Our Gallery</div>

<section class="newsletter">
  <span class="ring"><svg width="36" height="36" viewBox="0 0 36 36"><rect x="10" y="12" width="16" height="12" fill="none" stroke="#d6b24a" stroke-width="1.5"/><path d="m10 12 8 7 8-7" fill="none" stroke="#d6b24a" stroke-width="1.5"/></svg></span>
  <div class="title">NEWS &amp; OFFERS</div>
  <div class="input">your mail</div>
  <div class="btn">Sign Up</div>
  <span class="soc" style="left:904px"></span>
  <span class="soc" style="left:952px"></span>
  <span class="soc" style="left:1000px"></span>
  <span class="soc" style="left:1048px"></span>
  <span class="soc" style="left:1096px"></span>
</section>

<footer class="site-footer">
  <h5 style="left:69px">We Give Best Serives</h5>
  <p class="about-txt">Homemade cream cheese mints These are amazing! Made them last Christmas!!- must try!</p>
  <div class="contact" style="top:134px"><svg width="14" height="14" viewBox="0 0 20 20"><path d="M4 2h4l2 5-3 2a11 11 0 0 0 4 4l2-3 5 2v4a2 2 0 0 1-2 2A16 16 0 0 1 2 4a2 2 0 0 1 2-2z" fill="#fff"/></svg>1-555-204-7316</div>
  <div class="contact" style="top:168px"><svg width="14" height="16" viewBox="0 0 14 18"><path d="M7 0a7 7 0 0 1 7 7c0 5-7 11-7 11S0 12 0 7a7 7 0 0 1 7-7z" fill="#fff"/><circle cx="7" cy="7" r="2.5" fill="#1c1c1e"/></svg>212 Dune Walk Ln, Seaview 00000,<br>Florida (USA)</div>

  <h5 style="left:402px">QUICK LINKS</h5>
  <ul style="left:402px"><li>About</li><li>The Duplex</li><li>Gallery</li><li>Area Guide</li><li>Reviews</li><li>Contact Us</li></ul>

  <h5 style="left:616px">Property</h5>
  <ul style="left:616px"><li>Beachfront Duplex</li><li>1 Bedroom/ 2 Bathrooms</li><li>Sleeps 6</li><li>Full Kitchain</li><li>Free WI- Fi</li></ul>

  <h5 style="left:837px">Recent Blog</h5>
  <div class="blog" style="top:80px"><strong>Consectetur Adipisicing</strong><p>Lorem Ipsum is simply dummy text of the printing and typesetting industry.</p><div class="thumb" role="img" aria-label="Seaside hotel at dusk" style="background:linear-gradient(180deg,#2a3a5a,#8a9ab0 60%,#4a4a4a)"></div></div>
  <div class="blog" style="top:200px"><strong>Consectetur Adipisicing</strong><p>Lorem Ipsum is simply dummy text of the printing and typesetting industry.</p><div class="thumb" role="img" aria-label="Warmly lit hotel lobby" style="background:linear-gradient(180deg,#6a4a2a,#c8a070 55%,#3a2a1e)"></div></div>
</footer>

</body>
</html>
```